Bluefern Healthplan

We're designing a website to sell Medicare Supplements. Attached is an image of the words we want to say and general layout, but please use your best knowledge to make it better. This platform is intentionally simplistic because this is reaching an older demographic, so it should be very straightforward, attention-grabbing and extremely user-friendly, while still appearing reliable and professional.
Use your best judgement for color palate that conveys professional but approachable. Feel free to add imagery but don't overwhelm the page.
Updates
Designs look the same
Target Market(s)
65+ seniors
Number of Pages Required
1 page
Look and feel

```html
<!DOCTYPE html>
<html lang="en">
<head>
<meta charset="utf-8">
<title>Bluefern Healthplan – Home and Quote Dialog</title>
<link href="https://fonts.googleapis.com/css2?family=Roboto:wght@400;500;700&display=swap" rel="stylesheet">
<style>
:root{
  --blue:#1657b8;
  --green:#6cc12f;
  --ink:#1d1d1d;
  --muted:#7a7a7a;
  --line:#e3e5e8;
  --soft:#f1f1f2;
  --tile:#f6f7f9;
  --stage:#e9e9ec;
  --dark:#2b2b2b;
}
*{box-sizing:border-box;margin:0;padding:0}
html,body{width:844px;height:1200px;overflow:hidden;background:var(--stage);font-family:'Roboto',Arial,sans-serif;color:var(--ink)}
.stage{position:absolute;left:0;top:0;width:1614px;height:2296px;transform:scale(.5229);transform-origin:0 0}
.page{position:absolute;top:52px;width:646px;height:2166px;background:#fff;overflow:hidden}
.page--home{left:119px}
.page--dialog{left:849px}
.abs{position:absolute}
.center{text-align:center}

.site-header{left:0;top:0;width:646px;height:53px;border-top:3px solid var(--blue);background:#fff}
.brand{display:flex;align-items:center;gap:8px;font-weight:700;font-size:10.5px;color:var(--ink);white-space:nowrap}
.brand-dot{width:28px;height:28px;border-radius:50%;background:var(--blue);flex:none}
.nav{display:flex;gap:12px;font-size:8px;font-weight:500;white-space:nowrap}
.nav a{color:var(--ink);text-decoration:none;position:relative}
.nav a.is-active{color:var(--green)}
.nav a.is-active::after{content:"";position:absolute;left:-3px;right:-3px;top:14px;height:2px;background:var(--green)}
.call{display:flex;align-items:center;gap:6px}
.call small{display:block;font-size:6px;color:var(--muted)}
.call strong{display:block;font-size:8.5px;color:var(--blue);font-weight:500;white-space:nowrap}

.hero{left:0;top:53px;width:646px;height:312px;background:linear-gradient(100deg,#4f4d2e 0%,#7a6a3f 28%,#a69a86 52%,#6b8fbf 72%,#3d5f8c 100%)}
.hero-shade{left:0;top:53px;width:646px;height:312px;background:linear-gradient(90deg,rgba(30,30,20,.55) 0%,rgba(30,30,20,.25) 45%,rgba(0,0,0,0) 70%)}
.hero-title{left:60px;top:128px;font-size:22px;font-weight:500;color:#fff;white-space:nowrap}
.hero-lead{left:61px;top:163px;font-size:9.5px;line-height:13px;color:#fff;font-weight:500}
.btn{display:inline-flex;align-items:center;justify-content:center;gap:5px;height:27px;border-radius:14px;font-size:8px;font-weight:700;color:#fff;white-space:nowrap}
.btn--blue{background:var(--blue)}
.btn--green{background:var(--green)}
.btn--outline{border:1.5px solid #fff;background:transparent}
.plan-card{width:165px;height:138px;background:#fff;padding:4px}
.plan-photo{width:100%;height:106px}
.plan-caption{position:relative;height:28px;color:#fff;font-size:8px;font-weight:700;display:flex;align-items:flex-end;justify-content:center;padding-bottom:7px}
.plan-caption .badge{position:absolute;top:-17px;left:50%;margin-left:-16px;width:32px;height:32px;border-radius:50%;display:flex;align-items:center;justify-content:center}
.cap-blue{background:var(--blue)}.cap-blue .badge{background:var(--blue)}
.cap-dark{background:var(--dark)}.cap-dark .badge{background:var(--dark)}
.cap-green{background:var(--green)}.cap-green .badge{background:var(--green)}

.title{font-size:18px;font-weight:500;line-height:22px;color:var(--ink);width:646px;left:0;text-align:center}

.benefit{width:123px;height:118px;background:var(--tile);text-align:center;padding-top:8px}
.benefit h3{font-size:9px;font-weight:500;line-height:13px;margin-top:6px;padding:0 6px}
.benefit p{font-size:6.5px;line-height:10px;color:var(--muted);margin-top:5px;padding:0 8px}

.band-soft{background:var(--soft)}
.faq{width:253px;background:#fff;border:1px solid var(--line)}
.faq-q{height:24px;display:flex;align-items:center;gap:5px;padding:0 7px 0 10px;font-size:7.5px;font-weight:500;white-space:nowrap}
.faq-q span{flex:1}
.faq-a{font-size:6.5px;line-height:11px;color:var(--muted);padding:5px 12px 8px;border-top:1px solid var(--line)}
.toggle{width:7px;height:7px;border-radius:50%;background:var(--ink);position:relative;flex:none}
.toggle--open{background:var(--green)}
.toggle::after{content:"";position:absolute;left:2px;top:3px;width:3px;height:1px;background:#fff}

.cta{left:0;top:1019px;width:646px;height:159px;background:var(--blue)}
.cta h2{font-size:17px;font-weight:500;color:#fff}
.cta p{font-size:8.5px;color:#fff;font-weight:500}

.how-title{font-size:18px;font-weight:500;white-space:nowrap}
.how-lead{font-size:7.5px;line-height:12px;color:var(--muted);width:290px}
.step{width:160px;text-align:center}
.step-num{font-size:52px;font-weight:500;color:#e9e9e9;line-height:52px}
.step-icon{width:45px;height:45px;border-radius:50%;background:#474747;margin:-32px auto 0;position:relative;display:flex;align-items:center;justify-content:center}
.step h4{font-size:9.5px;font-weight:500;margin-top:15px;line-height:12px}
.step p{font-size:6.8px;line-height:12px;color:var(--muted);margin-top:5px}
.more{display:block;font-size:6.5px;font-weight:700;color:var(--green);margin-top:8px;letter-spacing:.2px}

.post{width:164px;height:193px;background:#fff;text-align:center;box-shadow:0 1px 3px rgba(0,0,0,.06)}
.post-photo{width:164px;height:95px}
.post h5{font-size:8.5px;font-weight:500;margin-top:11px}
.post-meta{font-size:6.3px;color:#555;margin-top:6px}
.post p{font-size:7px;line-height:11.5px;color:var(--muted);margin-top:7px;padding:0 6px}
.post .more{margin-top:6px}

.footer{left:0;top:1957px;width:646px;height:209px;background:var(--blue);color:#fff}
.footer .brand{color:#fff}
.footer .brand-dot{background:#fff}
.footer h6{font-size:9px;font-weight:500}
.footer ul{list-style:none;margin-top:10px}
.footer li{font-size:7px;line-height:18px;white-space:nowrap}
.footer li::before{content:"»";color:var(--green);margin-right:7px}
.contact-list li::before{content:none}
.contact-list li{display:flex;gap:8px;line-height:12px;margin-bottom:6px}
.contact-list i{display:inline-block;width:5px;height:6px;background:var(--green);border-radius:1px;margin-top:3px;flex:none}
.footer-about{font-size:7px;line-height:12px}
.social{display:flex;gap:3px}
.social span{width:18px;height:18px;border:1px solid #fff;border-radius:50%}
.rule{left:56px;top:2128px;width:541px;height:1px;background:rgba(255,255,255,.35)}
.copyright{font-size:7px}

.overlay{left:0;top:0;width:646px;height:2166px;background:rgba(20,22,28,.52)}
.dialog{left:129px;top:161px;width:387px;height:250px;background:#eef0f3}
.dialog h2{font-size:14px;font-weight:500;text-align:center;padding-top:18px}
.dialog-close{right:16px;top:19px;font-size:11px;color:#888}
.dialog-rule{left:10px;top:51px;width:367px;height:1px;background:#dcdfe3}
.dialog-split{left:193px;top:70px;width:1px;height:165px;background:#d6dade}
.or{left:178px;top:128px;width:30px;height:30px;border-radius:50%;background:var(--blue);color:#fff;font-size:8px;font-weight:700;display:flex;align-items:center;justify-content:center}
.dialog h3{font-size:13px;font-weight:500;color:var(--blue)}
.dialog p{font-size:7px;line-height:13px;color:#555}
.dialog .phone{color:var(--blue);font-weight:700;font-size:8px}
</style>
</head>
<body>
<div class="stage">

<!-- ======= Home page ======= -->
<section class="page page--home">
  <header class="abs site-header">
    <div class="abs brand" style="left:60px;top:10px"><span class="brand-dot"></span>Bluefern Healthplan</div>
    <nav class="abs nav" style="left:259px;top:20px"><a class="is-active">Home</a><a>About</a><a>Medicare ▾</a><a>Blog</a><a>Contact Us</a></nav>
    <div class="abs call" style="left:495px;top:13px">
      <svg width="18" height="18" viewBox="0 0 18 18"><circle cx="9" cy="9" r="8" fill="none" stroke="#6cc12f" stroke-width="1.2"/><path d="M6 5.5l1.5-.5 1 2-1 .8a5 5 0 0 0 2.7 2.7l.8-1 2 1-.5 1.5c-3.5.3-6.8-3-6.5-6.5z" fill="#1657b8"/></svg>
      <div><small>Call Us Now</small><strong>(555) 210-4400</strong></div>
    </div>
  </header>

  <div class="abs hero" role="img" aria-label="Photo of a smiling senior couple looking at a tablet together outdoors"></div>
  <div class="abs hero-shade"></div>
  <h1 class="abs hero-title">Bluefern Healthplan</h1>
  <p class="abs hero-lead">Be confident in choosing the Medicare Supplement<br>plan that’s right for you.</p>
  <span class="abs btn btn--blue" style="left:62px;top:208px;width:84px">
    <svg width="6" height="8" viewBox="0 0 6 8"><path d="M3 0a3 3 0 0 1 3 3c0 2-3 5-3 5S0 5 0 3a3 3 0 0 1 3-3z" fill="#fff"/></svg>641018</span>
  <span class="abs btn btn--green" style="left:154px;top:208px;width:110px">GET FREE QUOTES
    <svg width="8" height="8" viewBox="0 0 8 8"><circle cx="4" cy="4" r="4" fill="#fff"/><path d="M3 2l2 2-2 2" fill="none" stroke="#6cc12f" stroke-width="1.2"/></svg></span>

  <div class="abs plan-card" style="left:60px;top:298px">
    <div class="plan-photo" role="img" aria-label="Photo of a senior couple reviewing paperwork at home" style="background:linear-gradient(135deg,#cfc8be,#8a7f74 60%,#5b5750)"></div>
    <div class="plan-caption cap-blue"><span class="badge"><svg width="14" height="14" viewBox="0 0 14 14" fill="none" stroke="#fff"><rect x="2" y="3" width="10" height="9"/><path d="M5 7h4M7 5v4"/></svg></span>Medicare Supplement</div>
  </div>
  <div class="abs plan-card" style="left:241px;top:298px">
    <div class="plan-photo" role="img" aria-label="Photo of a group of seniors talking together" style="background:linear-gradient(135deg,#7a7268,#b9b0a3 55%,#574f47)"></div>
    <div class="plan-caption cap-dark"><span class="badge"><svg width="14" height="14" viewBox="0 0 14 14" fill="none" stroke="#fff"><rect x="3" y="2" width="8" height="10"/><path d="M5 5h4M5 8h4"/></svg></span>Medicare Part D</div>
  </div>
  <div class="abs plan-card" style="left:421px;top:298px">
    <div class="plan-photo" role="img" aria-label="Photo of a smiling senior couple relaxing on a sofa" style="background:linear-gradient(135deg,#e7e3d6,#c9bfa5 55%,#9db3c7)"></div>
    <div class="plan-caption cap-green"><span class="badge"><svg width="14" height="14" viewBox="0 0 14 14" fill="none" stroke="#fff"><circle cx="7" cy="6" r="4"/><path d="M5 12h4"/></svg></span>Medicare Advantage</div>
  </div>

  <h2 class="abs title" style="top:497px">Understanding The Benefits of<br>Medicare Insurance</h2>
  <div class="abs benefit" style="left:60px;top:564px">
    <svg width="34" height="30" viewBox="0 0 34 30" fill="none" stroke="#1657b8" stroke-width="1.2"><rect x="3" y="6" width="26" height="20" rx="2"/><path d="M3 11h26"/><circle cx="24" cy="21" r="5" stroke="#6cc12f"/></svg>
    <h3>bluefernhealthplan is FREE to Use</h3>
    <p>Lorem ipsum dolor sit amet, consectetur adipiscing elit, sed do eiusmod tempor</p>
  </div>
  <div class="abs benefit" style="left:194px;top:564px">
    <svg width="34" height="30" viewBox="0 0 34 30" fill="none" stroke="#1657b8" stroke-width="1.2"><rect x="6" y="2" width="22" height="18" rx="2"/><circle cx="17" cy="11" r="5" stroke="#6cc12f"/><path d="M11 28l6-8 6 8"/></svg>
    <h3>We help you save time</h3>
    <p>Lorem ipsum dolor sit amet, consectetur adipiscing elit, sed do eiusmod tempor</p>
  </div>
  <div class="abs benefit" style="left:329px;top:564px">
    <svg width="34" height="30" viewBox="0 0 34 30" fill="none" stroke="#1657b8" stroke-width="1.2"><rect x="9" y="2" width="17" height="25" rx="1"/><path d="M13 8h9M13 12h9M13 16h6"/><circle cx="11" cy="22" r="4" stroke="#6cc12f"/></svg>
    <h3>Plan recommendation</h3>
    <p>Lorem ipsum dolor sit amet, consectetur adipiscing elit, sed do eiusmod tempor</p>
  </div>
  <div class="abs benefit" style="left:463px;top:564px">
    <svg width="34" height="30" viewBox="0 0 34 30" fill="none" stroke="#1657b8" stroke-width="1.2"><path d="M7 16a10 10 0 0 1 20 0"/><rect x="4" y="15" width="5" height="8" rx="2"/><rect x="25" y="15" width="5" height="8" rx="2"/><circle cx="17" cy="17" r="5" stroke="#6cc12f"/></svg>
    <h3>Talk to a U.S. based, licensed expert</h3>
    <p>Lorem ipsum dolor sit amet, consectetur adipiscing elit, sed do eiusmod tempor</p>
  </div>

  <div class="abs band-soft" style="left:0;top:735px;width:646px;height:284px"></div>
  <h2 class="abs title" style="top:763px">Frequently Asked Questions</h2>
  <div class="abs faq" style="left:60px;top:811px">
    <div class="faq-q"><svg width="8" height="7" viewBox="0 0 8 7"><path d="M4 0C1.8 0 0 1.3 0 3c0 .8.4 1.5 1 2L.5 7 3 5.9c.3.1.6.1 1 .1 2.2 0 4-1.3 4-3S6.2 0 4 0z" fill="#1657b8"/></svg><span>Lorem ipsum dolor sit amet, consectetur elit</span><i class="toggle toggle--open"></i></div>
    <div class="faq-a">Sed ut perspiciatis unde omnis iste natus error sit voluptatem accusantium doloremque laudantium, totam rem aperiam, eaque ipsa quae ab illo inventore</div>
  </div>
  <div class="abs faq" style="left:60px;top:902px"><div class="faq-q"><svg width="8" height="7" viewBox="0 0 8 7"><path d="M4 0C1.8 0 0 1.3 0 3c0 .8.4 1.5 1 2L.5 7 3 5.9c.3.1.6.1 1 .1 2.2 0 4-1.3 4-3S6.2 0 4 0z" fill="#1657b8"/></svg><span>Lorem ipsum dolor sit amet, consectetur elit</span><i class="toggle"></i></div></div>
  <div class="abs faq" style="left:60px;top:942px"><div class="faq-q"><svg width="8" height="7" viewBox="0 0 8 7"><path d="M4 0C1.8 0 0 1.3 0 3c0 .8.4 1.5 1 2L.5 7 3 5.9c.3.1.6.1 1 .1 2.2 0 4-1.3 4-3S6.2 0 4 0z" fill="#1657b8"/></svg><span>Lorem ipsum dolor sit amet, consectetur elit</span><i class="toggle"></i></div></div>
  <div class="abs faq" style="left:332px;top:811px"><div class="faq-q"><svg width="8" height="7" viewBox="0 0 8 7"><path d="M4 0C1.8 0 0 1.3 0 3c0 .8.4 1.5 1 2L.5 7 3 5.9c.3.1.6.1 1 .1 2.2 0 4-1.3 4-3S6.2 0 4 0z" fill="#1657b8"/></svg><span>Lorem ipsum dolor sit amet, consectetur elit</span><i class="toggle"></i></div></div>
  <div class="abs faq" style="left:332px;top:852px"><div class="faq-q"><svg width="8" height="7" viewBox="0 0 8 7"><path d="M4 0C1.8 0 0 1.3 0 3c0 .8.4 1.5 1 2L.5 7 3 5.9c.3.1.6.1 1 .1 2.2 0 4-1.3 4-3S6.2 0 4 0z" fill="#1657b8"/></svg><span>Lorem ipsum dolor sit amet, consectetur elit</span><i class="toggle"></i></div></div>
  <div class="abs faq" style="left:332px;top:893px">
    <div class="faq-q"><svg width="8" height="7" viewBox="0 0 8 7"><path d="M4 0C1.8 0 0 1.3 0 3c0 .8.4 1.5 1 2L.5 7 3 5.9c.3.1.6.1 1 .1 2.2 0 4-1.3 4-3S6.2 0 4 0z" fill="#1657b8"/></svg><span>Lorem ipsum dolor sit amet, consectetur elit</span><i class="toggle toggle--open"></i></div>
    <div class="faq-a">Sed ut perspiciatis unde omnis iste natus error sit voluptatem accusantium doloremque laudantium, totam rem aperiam, eaque ipsa quae ab illo inventore</div>
  </div>

  <div class="abs cta">
    <h2 class="abs center" style="left:0;top:33px;width:646px">Get a Free Medicare Quote</h2>
    <p class="abs center" style="left:0;top:65px;width:646px">Be confident in choosing the Medicare Supplement plan that’s right for you.</p>
    <span class="abs btn btn--outline" style="left:221px;top:96px;width:86px">
      <svg width="6" height="8" viewBox="0 0 6 8"><path d="M3 0a3 3 0 0 1 3 3c0 2-3 5-3 5S0 5 0 3a3 3 0 0 1 3-3z" fill="#fff"/></svg>641018</span>
    <span class="abs btn btn--green" style="left:314px;top:96px;width:110px">GET FREE QUOTES
      <svg width="8" height="8" viewBox="0 0 8 8"><circle cx="4" cy="4" r="4" fill="#fff"/><path d="M3 2l2 2-2 2" fill="none" stroke="#6cc12f" stroke-width="1.2"/></svg></span>
  </div>

  <h2 class="abs how-title" style="left:60px;top:1225px">How Medicare works</h2>
  <p class="abs how-lead" style="left:281px;top:1227px">Sed ut perspiciatis unde omnis iste natus error sit voluptatem doloremque laudantium, totam rem aperiam, eaque ipsa quae</p>
  <div class="abs step" style="left:60px;top:1262px"><div class="step-num">1</div><div class="step-icon"><svg width="22" height="22" viewBox="0 0 22 22" fill="none" stroke="#fff"><rect x="4" y="5" width="14" height="15"/><path d="M9 9h4M11 7v4M8 20v-4h6v4"/></svg></div><h4>Hospital &amp; Inpatient</h4><p>Lorem ipsum dolor sit amet, consectetur adipiscing elit, sed do eiusmod</p><span class="more">LEARN MORE »</span></div>
  <div class="abs step" style="left:243px;top:1262px"><div class="step-num">2</div><div class="step-icon"><svg width="22" height="22" viewBox="0 0 22 22" fill="none" stroke="#fff"><rect x="3" y="7" width="12" height="12"/><circle cx="15" cy="8" r="4"/><path d="M6 12h6M6 15h6"/></svg></div><h4>Doctors &amp; Medical</h4><p>Lorem ipsum dolor sit amet, consectetur adipiscing elit, sed do eiusmod</p><span class="more">LEARN MORE »</span></div>
  <div class="abs step" style="left:426px;top:1262px"><div class="step-num">3</div><div class="step-icon"><svg width="22" height="22" viewBox="0 0 22 22" fill="none" stroke="#fff"><rect x="5" y="4" width="12" height="16"/><path d="M9 8h4M8 12h2M12 12h2M9 20v-4h4v4"/></svg></div><h4>Medicare Advantage</h4><p>Lorem ipsum dolor sit amet, consectetur adipiscing elit, sed do eiusmod</p><span class="more">LEARN MORE »</span></div>
  <div class="abs step" style="left:142px;top:1419px"><div class="step-num">4</div><div class="step-icon"><svg width="22" height="22" viewBox="0 0 22 22" fill="none" stroke="#fff"><rect x="4" y="7" width="10" height="12" rx="1"/><path d="M7 13h4M9 11v4M6 4h6v3"/><circle cx="16" cy="16" r="3"/></svg></div><h4>Medicare Prescription Drug</h4><p>Lorem ipsum dolor sit amet, consectetur adipiscing elit, sed do eiusmod</p><span class="more">LEARN MORE »</span></div>
  <div class="abs step" style="left:343px;top:1419px"><div class="step-num">5</div><div class="step-icon"><svg width="22" height="22" viewBox="0 0 22 22" fill="none" stroke="#fff"><path d="M11 3l7 3v5c0 5-3 7-7 9-4-2-7-4-7-9V6z"/><path d="M8 11l2 2 4-4"/></svg></div><h4>Supplement also called<br>Bluefern Healthplan</h4><p>Lorem ipsum dolor sit amet, consectetur adipiscing elit, sed do eiusmod</p><span class="more">LEARN MORE »</span></div>

  <div class="abs band-soft" style="left:0;top:1641px;width:646px;height:316px"></div>
  <h2 class="abs title" style="top:1670px">Our Blog</h2>
  <article class="abs post" style="left:60px;top:1710px"><div class="post-photo" role="img" aria-label="Photo of a doctor filling in a medical form on a clipboard" style="background:linear-gradient(135deg,#dfe6ee,#b9c7d6 60%,#6d7c8f)"></div><h5>Lorem ipsum dolor consectetur</h5><div class="post-meta">▣ 13 April 2020 &nbsp;|&nbsp; ● By John Doe</div><p>Sed ut perspiciatis unde omnis iste natus error sit voluptatem accusantium</p><span class="more">READ MORE ➜</span></article>
  <article class="abs post" style="left:241px;top:1710px"><div class="post-photo" role="img" aria-label="Photo of a doctor consulting with a senior woman in a bright office" style="background:linear-gradient(135deg,#f2f1ec,#d9d6cc 55%,#b7b3a4)"></div><h5>Lorem ipsum dolor consectetur</h5><div class="post-meta">▣ 27 March 2020 &nbsp;|&nbsp; ● By John Doe</div><p>Sed ut perspiciatis unde omnis iste natus error sit voluptatem accusantium</p><span class="more">READ MORE ➜</span></article>
  <article class="abs post" style="left:421px;top:1710px"><div class="post-photo" role="img" aria-label="Photo of a senior man talking with a nurse" style="background:linear-gradient(135deg,#8c5f55,#c3b4aa 50%,#4f83a9)"></div><h5>Lorem ipsum dolor consectetur</h5><div class="post-meta">▣ 20 March 2020 &nbsp;|&nbsp; ● By John Doe</div><p>Sed ut perspiciatis unde omnis iste natus error sit voluptatem accusantium</p><span class="more">READ MORE ➜</span></article>

  <footer class="abs footer">
    <div class="abs brand" style="left:60px;top:34px"><span class="brand-dot"></span>Bluefern Healthplan</div>
    <p class="abs footer-about" style="left:60px;top:78px">Lorem ipsum dolor sit consectetur<br>adipiscing elit, sed do eiusmod<br>tempor incididunt</p>
    <div class="abs social" style="left:60px;top:124px"><span></span><span></span><span></span><span></span></div>
    <div class="abs" style="left:245px;top:30px"><h6>Company</h6><ul><li>Home</li><li>About Us</li><li>Blog</li><li>Medicare Plans</li><li>Affiliate Program</li></ul></div>
    <div class="abs" style="left:352px;top:30px"><h6>Resources</h6><ul><li>Reviews</li><li>FAQ</li><li>Support</li><li>Links</li><li>Term of Use</li></ul></div>
    <div class="abs" style="left:455px;top:30px"><h6>Contact us</h6><ul class="contact-list"><li><i></i>123, Lorem ipsum dolor amet,<br>consectetur elit</li><li><i></i>(555) 444-5678</li><li><i></i>555 210 4401</li><li><i></i>info@bluefernhealthplan.com</li></ul></div>
  </footer>
  <div class="abs rule"></div>
  <p class="abs copyright center" style="left:0;top:2141px;width:646px;color:#fff">© 2020 Bluefern Healthplan | All Rights Reserved</p>
</section>

<!-- ======= Home page with quote dialog ======= -->
<section class="page page--dialog">
  <header class="abs site-header">
    <div class="abs brand" style="left:60px;top:10px"><span class="brand-dot"></span>Bluefern Healthplan</div>
    <nav class="abs nav" style="left:259px;top:20px"><a class="is-active">Home</a><a>About</a><a>Medicare ▾</a><a>Blog</a><a>Contact Us</a></nav>
    <div class="abs call" style="left:495px;top:13px">
      <svg width="18" height="18" viewBox="0 0 18 18"><circle cx="9" cy="9" r="8" fill="none" stroke="#6cc12f" stroke-width="1.2"/><path d="M6 5.5l1.5-.5 1 2-1 .8a5 5 0 0 0 2.7 2.7l.8-1 2 1-.5 1.5c-3.5.3-6.8-3-6.5-6.5z" fill="#1657b8"/></svg>
      <div><small>Call Us Now</small><strong>(555) 210-4400</strong></div>
    </div>
  </header>

  <div class="abs hero" role="img" aria-label="Photo of a smiling senior couple looking at a tablet together outdoors"></div>
  <div class="abs hero-shade"></div>
  <h1 class="abs hero-title">Bluefern Healthplan</h1>
  <p class="abs hero-lead">Be confident in choosing the Medicare Supplement<br>plan that’s right for you.</p>
  <span class="abs btn btn--blue" style="left:62px;top:208px;width:84px">
    <svg width="6" height="8" viewBox="0 0 6 8"><path d="M3 0a3 3 0 0 1 3 3c0 2-3 5-3 5S0 5 0 3a3 3 0 0 1 3-3z" fill="#fff"/></svg>641018</span>
  <span class="abs btn btn--green" style="left:154px;top:208px;width:110px">GET FREE QUOTES
    <svg width="8" height="8" viewBox="0 0 8 8"><circle cx="4" cy="4" r="4" fill="#fff"/><path d="M3 2l2 2-2 2" fill="none" stroke="#6cc12f" stroke-width="1.2"/></svg></span>

  <div class="abs plan-card" style="left:60px;top:298px">
    <div class="plan-photo" role="img" aria-label="Photo of a senior couple reviewing paperwork at home" style="background:linear-gradient(135deg,#cfc8be,#8a7f74 60%,#5b5750)"></div>
    <div class="plan-caption cap-blue"><span class="badge"><svg width="14" height="14" viewBox="0 0 14 14" fill="none" stroke="#fff"><rect x="2" y="3" width="10" height="9"/><path d="M5 7h4M7 5v4"/></svg></span>Medicare Supplement</div>
  </div>
  <div class="abs plan-card" style="left:241px;top:298px">
    <div class="plan-photo" role="img" aria-label="Photo of a group of seniors talking together" style="background:linear-gradient(135deg,#7a7268,#b9b0a3 55%,#574f47)"></div>
    <div class="plan-caption cap-dark"><span class="badge"><svg width="14" height="14" viewBox="0 0 14 14" fill="none" stroke="#fff"><rect x="3" y="2" width="8" height="10"/><path d="M5 5h4M5 8h4"/></svg></span>Medicare Part D</div>
  </div>
  <div class="abs plan-card" style="left:421px;top:298px">
    <div class="plan-photo" role="img" aria-label="Photo of a smiling senior couple relaxing on a sofa" style="background:linear-gradient(135deg,#e7e3d6,#c9bfa5 55%,#9db3c7)"></div>
    <div class="plan-caption cap-green"><span class="badge"><svg width="14" height="14" viewBox="0 0 14 14" fill="none" stroke="#fff"><circle cx="7" cy="6" r="4"/><path d="M5 12h4"/></svg></span>Medicare Advantage</div>
  </div>

  <h2 class="abs title" style="top:497px">Understanding The Benefits of<br>Medicare Insurance</h2>
  <div class="abs benefit" style="left:60px;top:564px"><svg width="34" height="30" viewBox="0 0 34 30" fill="none" stroke="#1657b8" stroke-width="1.2"><rect x="3" y="6" width="26" height="20" rx="2"/><path d="M3 11h26"/><circle cx="24" cy="21" r="5" stroke="#6cc12f"/></svg><h3>bluefernhealthplan is FREE to Use</h3><p>Lorem ipsum dolor sit amet, consectetur adipiscing elit, sed do eiusmod tempor</p></div>
  <div class="abs benefit" style="left:194px;top:564px"><svg width="34" height="30" viewBox="0 0 34 30" fill="none" stroke="#1657b8" stroke-width="1.2"><rect x="6" y="2" width="22" height="18" rx="2"/><circle cx="17" cy="11" r="5" stroke="#6cc12f"/><path d="M11 28l6-8 6 8"/></svg><h3>We help you save time</h3><p>Lorem ipsum dolor sit amet, consectetur adipiscing elit, sed do eiusmod tempor</p></div>
  <div class="abs benefit" style="left:329px;top:564px"><svg width="34" height="30" viewBox="0 0 34 30" fill="none" stroke="#1657b8" stroke-width="1.2"><rect x="9" y="2" width="17" height="25" rx="1"/><path d="M13 8h9M13 12h9M13 16h6"/><circle cx="11" cy="22" r="4" stroke="#6cc12f"/></svg><h3>Plan recommendation</h3><p>Lorem ipsum dolor sit amet, consectetur adipiscing elit, sed do eiusmod tempor</p></div>
  <div class="abs benefit" style="left:463px;top:564px"><svg width="34" height="30" viewBox="0 0 34 30" fill="none" stroke="#1657b8" stroke-width="1.2"><path d="M7 16a10 10 0 0 1 20 0"/><rect x="4" y="15" width="5" height="8" rx="2"/><rect x="25" y="15" width="5" height="8" rx="2"/><circle cx="17" cy="17" r="5" stroke="#6cc12f"/></svg><h3>Talk to a U.S. based, licensed expert</h3><p>Lorem ipsum dolor sit amet, consectetur adipiscing elit, sed do eiusmod tempor</p></div>

  <div class="abs band-soft" style="left:0;top:735px;width:646px;height:284px"></div>
  <h2 class="abs title" style="top:763px">Frequently Asked Questions</h2>
  <div class="abs faq" style="left:60px;top:811px"><div class="faq-q"><svg width="8" height="7" viewBox="0 0 8 7"><path d="M4 0C1.8 0 0 1.3 0 3c0 .8.4 1.5 1 2L.5 7 3 5.9c.3.1.6.1 1 .1 2.2 0 4-1.3 4-3S6.2 0 4 0z" fill="#1657b8"/></svg><span>Lorem ipsum dolor sit amet, consectetur elit</span><i class="toggle toggle--open"></i></div><div class="faq-a">Sed ut perspiciatis unde omnis iste natus error sit voluptatem accusantium doloremque laudantium, totam rem aperiam, eaque ipsa quae ab illo inventore</div></div>
  <div class="abs faq" style="left:60px;top:902px"><div class="faq-q"><svg width="8" height="7" viewBox="0 0 8 7"><path d="M4 0C1.8 0 0 1.3 0 3c0 .8.4 1.5 1 2L.5 7 3 5.9c.3.1.6.1 1 .1 2.2 0 4-1.3 4-3S6.2 0 4 0z" fill="#1657b8"/></svg><span>Lorem ipsum dolor sit amet, consectetur elit</span><i class="toggle"></i></div></div>
  <div class="abs faq" style="left:60px;top:942px"><div class="faq-q"><svg width="8" height="7" viewBox="0 0 8 7"><path d="M4 0C1.8 0 0 1.3 0 3c0 .8.4 1.5 1 2L.5 7 3 5.9c.3.1.6.1 1 .1 2.2 0 4-1.3 4-3S6.2 0 4 0z" fill="#1657b8"/></svg><span>Lorem ipsum dolor sit amet, consectetur elit</span><i class="toggle"></i></div></div>
  <div class="abs faq" style="left:332px;top:811px"><div class="faq-q"><svg width="8" height="7" viewBox="0 0 8 7"><path d="M4 0C1.8 0 0 1.3 0 3c0 .8.4 1.5 1 2L.5 7 3 5.9c.3.1.6.1 1 .1 2.2 0 4-1.3 4-3S6.2 0 4 0z" fill="#1657b8"/></svg><span>Lorem ipsum dolor sit amet, consectetur elit</span><i class="toggle"></i></div></div>
  <div class="abs faq" style="left:332px;top:852px"><div class="faq-q"><svg width="8" height="7" viewBox="0 0 8 7"><path d="M4 0C1.8 0 0 1.3 0 3c0 .8.4 1.5 1 2L.5 7 3 5.9c.3.1.6.1 1 .1 2.2 0 4-1.3 4-3S6.2 0 4 0z" fill="#1657b8"/></svg><span>Lorem ipsum dolor sit amet, consectetur elit</span><i class="toggle"></i></div></div>
  <div class="abs faq" style="left:332px;top:893px"><div class="faq-q"><svg width="8" height="7" viewBox="0 0 8 7"><path d="M4 0C1.8 0 0 1.3 0 3c0 .8.4 1.5 1 2L.5 7 3 5.9c.3.1.6.1 1 .1 2.2 0 4-1.3 4-3S6.2 0 4 0z" fill="#1657b8"/></svg><span>Lorem ipsum dolor sit amet, consectetur elit</span><i class="toggle toggle--open"></i></div><div class="faq-a">Sed ut perspiciatis unde omnis iste natus error sit voluptatem accusantium doloremque laudantium, totam rem aperiam, eaque ipsa quae ab illo inventore</div></div>

  <div class="abs cta">
    <h2 class="abs center" style="left:0;top:33px;width:646px">Get a Free Medicare Quote</h2>
    <p class="abs center" style="left:0;top:65px;width:646px">Be confident in choosing the Medicare Supplement plan that’s right for you.</p>
    <span class="abs btn btn--outline" style="left:221px;top:96px;width:86px">
      <svg width="6" height="8" viewBox="0 0 6 8"><path d="M3 0a3 3 0 0 1 3 3c0 2-3 5-3 5S0 5 0 3a3 3 0 0 1 3-3z" fill="#fff"/></svg>641018</span>
    <span class="abs btn btn--green" style="left:314px;top:96px;width:110px">GET FREE QUOTES
      <svg width="8" height="8" viewBox="0 0 8 8"><circle cx="4" cy="4" r="4" fill="#fff"/><path d="M3 2l2 2-2 2" fill="none" stroke="#6cc12f" stroke-width="1.2"/></svg></span>
  </div>

  <h2 class="abs how-title" style="left:60px;top:1225px">How Medicare works</h2>
  <p class="abs how-lead" style="left:281px;top:1227px">Sed ut perspiciatis unde omnis iste natus error sit voluptatem doloremque laudantium, totam rem aperiam, eaque ipsa quae</p>
  <div class="abs step" style="left:60px;top:1262px"><div class="step-num">1</div><div class="step-icon"><svg width="22" height="22" viewBox="0 0 22 22" fill="none" stroke="#fff"><rect x="4" y="5" width="14" height="15"/><path d="M9 9h4M11 7v4M8 20v-4h6v4"/></svg></div><h4>Hospital &amp; Inpatient</h4><p>Lorem ipsum dolor sit amet, consectetur adipiscing elit, sed do eiusmod</p><span class="more">LEARN MORE »</span></div>
  <div class="abs step" style="left:243px;top:1262px"><div class="step-num">2</div><div class="step-icon"><svg width="22" height="22" viewBox="0 0 22 22" fill="none" stroke="#fff"><rect x="3" y="7" width="12" height="12"/><circle cx="15" cy="8" r="4"/><path d="M6 12h6M6 15h6"/></svg></div><h4>Doctors &amp; Medical</h4><p>Lorem ipsum dolor sit amet, consectetur adipiscing elit, sed do eiusmod</p><span class="more">LEARN MORE »</span></div>
  <div class="abs step" style="left:426px;top:1262px"><div class="step-num">3</div><div class="step-icon"><svg width="22" height="22" viewBox="0 0 22 22" fill="none" stroke="#fff"><rect x="5" y="4" width="12" height="16"/><path d="M9 8h4M8 12h2M12 12h2M9 20v-4h4v4"/></svg></div><h4>Medicare Advantage</h4><p>Lorem ipsum dolor sit amet, consectetur adipiscing elit, sed do eiusmod</p><span class="more">LEARN MORE »</span></div>
  <div class="abs step" style="left:142px;top:1419px"><div class="step-num">4</div><div class="step-icon"><svg width="22" height="22" viewBox="0 0 22 22" fill="none" stroke="#fff"><rect x="4" y="7" width="10" height="12" rx="1"/><path d="M7 13h4M9 11v4M6 4h6v3"/><circle cx="16" cy="16" r="3"/></svg></div><h4>Medicare Prescription Drug</h4><p>Lorem ipsum dolor sit amet, consectetur adipiscing elit, sed do eiusmod</p><span class="more">LEARN MORE »</span></div>
  <div class="abs step" style="left:343px;top:1419px"><div class="step-num">5</div><div class="step-icon"><svg width="22" height="22" viewBox="0 0 22 22" fill="none" stroke="#fff"><path d="M11 3l7 3v5c0 5-3 7-7 9-4-2-7-4-7-9V6z"/><path d="M8 11l2 2 4-4"/></svg></div><h4>Supplement also called<br>Bluefern Healthplan</h4><p>Lorem ipsum dolor sit amet, consectetur adipiscing elit, sed do eiusmod</p><span class="more">LEARN MORE »</span></div>

  <div class="abs band-soft" style="left:0;top:1641px;width:646px;height:316px"></div>
  <h2 class="abs title" style="top:1670px">Our Blog</h2>
  <article class="abs post" style="left:60px;top:1710px"><div class="post-photo" role="img" aria-label="Photo of a doctor filling in a medical form on a clipboard" style="background:linear-gradient(135deg,#dfe6ee,#b9c7d6 60%,#6d7c8f)"></div><h5>Lorem ipsum dolor consectetur</h5><div class="post-meta">▣ 13 April 2020 &nbsp;|&nbsp; ● By John Doe</div><p>Sed ut perspiciatis unde omnis iste natus error sit voluptatem accusantium</p><span class="more">READ MORE ➜</span></article>
  <article class="abs post" style="left:241px;top:1710px"><div class="post-photo" role="img" aria-label="Photo of a doctor consulting with a senior woman in a bright office" style="background:linear-gradient(135deg,#f2f1ec,#d9d6cc 55%,#b7b3a4)"></div><h5>Lorem ipsum dolor consectetur</h5><div class="post-meta">▣ 27 March 2020 &nbsp;|&nbsp; ● By John Doe</div><p>Sed ut perspiciatis unde omnis iste natus error sit voluptatem accusantium</p><span class="more">READ MORE ➜</span></article>
  <article class="abs post" style="left:421px;top:1710px"><div class="post-photo" role="img" aria-label="Photo of a senior man talking with a nurse" style="background:linear-gradient(135deg,#8c5f55,#c3b4aa 50%,#4f83a9)"></div><h5>Lorem ipsum dolor consectetur</h5><div class="post-meta">▣ 20 March 2020 &nbsp;|&nbsp; ● By John Doe</div><p>Sed ut perspiciatis unde omnis iste natus error sit voluptatem accusantium</p><span class="more">READ MORE ➜</span></article>

  <footer class="abs footer">
    <div class="abs brand" style="left:60px;top:34px"><span class="brand-dot"></span>Bluefern Healthplan</div>
    <p class="abs footer-about" style="left:60px;top:78px">Lorem ipsum dolor sit consectetur<br>adipiscing elit, sed do eiusmod<br>tempor incididunt</p>
    <div class="abs social" style="left:60px;top:124px"><span></span><span></span><span></span><span></span></div>
    <div class="abs" style="left:245px;top:30px"><h6>Company</h6><ul><li>Home</li><li>About Us</li><li>Blog</li><li>Medicare Plans</li><li>Affiliate Program</li></ul></div>
    <div class="abs" style="left:352px;top:30px"><h6>Resources</h6><ul><li>Reviews</li><li>FAQ</li><li>Support</li><li>Links</li><li>Term of Use</li></ul></div>
    <div class="abs" style="left:455px;top:30px"><h6>Contact us</h6><ul class="contact-list"><li><i></i>123, Lorem ipsum dolor amet,<br>consectetur elit</li><li><i></i>(555) 444-5678</li><li><i></i>555 210 4401</li><li><i></i>info@bluefernhealthplan.com</li></ul></div>
  </footer>
  <div class="abs rule"></div>
  <p class="abs copyright center" style="left:0;top:2141px;width:646px;color:#fff">© 2020 Bluefern Healthplan | All Rights Reserved</p>

  <div class="abs overlay"></div>

  <div class="abs dialog" role="dialog" aria-label="Free Medicare Insurance Quote">
    <h2>Free Medicare Insurance Quote</h2>
    <span class="abs dialog-close">X</span>
    <div class="abs dialog-rule"></div>
    <div class="abs dialog-split"></div>
    <div class="abs center" style="left:20px;top:75px;width:168px">
      <h3>Online</h3>
      <p style="margin-top:4px">Our easy tool lets you compare<br>quotes from top providers, all<br>at once!</p>
      <span class="btn btn--blue" style="width:104px;height:26px;margin-top:8px">
        <svg width="6" height="8" viewBox="0 0 6 8"><path d="M3 0a3 3 0 0 1 3 3c0 2-3 5-3 5S0 5 0 3a3 3 0 0 1 3-3z" fill="#fff"/></svg>641018</span><br>
      <span class="btn btn--green" style="width:110px;height:26px;margin-top:8px">GET FREE QUOTES
        <svg width="8" height="8" viewBox="0 0 8 8"><circle cx="4" cy="4" r="4" fill="#fff"/><path d="M3 2l2 2-2 2" fill="none" stroke="#6cc12f" stroke-width="1.2"/></svg></span>
    </div>
    <div class="abs or">OR</div>
    <div class="abs center" style="left:210px;top:88px;width:160px">
      <svg width="28" height="26" viewBox="0 0 28 26" fill="none" stroke="#1657b8" stroke-width="1.2"><path d="M5 14a9 9 0 0 1 18 0"/><rect x="2" y="13" width="5" height="8" rx="2"/><rect x="21" y="13" width="5" height="8" rx="2"/><circle cx="14" cy="14" r="5"/></svg>
      <p style="margin-top:10px">And talk to a live agent to help you<br>find the right plan!</p>
      <p style="margin-top:10px">Call <span class="phone">(555) 318-7720</span></p>
    </div>
  </div>
</section>

</div>
</body>
</html>
```